Gather Every Thread Book Cover Design

We need:

Ebook and 6x 9 Inch trade paperback book cover (front, back, spine)

Book Title:Gather Every Thread
Subtitle: Getting Ready Before Hard Times Strike (Including Final Goodbyes) for Every Household

For a book written to help any of us gather the information needed to ensure we are set to take care of our loved ones in case of an emergency. Loved ones, a sense of urgency that leads to feeling calm and prepared is needed!

Target Market(s)

Any adult with children, a partner, parents or assets!

Industry/Entity Type

Financial Planning, Health care, Family

Font styles to use
Serif
Sans Serif

Colors
0054AA
0677BA
7BADD7
CADEEF
E8F1F8
FFF300
FFF600
FEFA6F
FFFEC7
FFFEE8
EE7325
F08F49
F5BC92
FAE3D3
FDF4ED
EB3D1F
EC4F4E
F09395
F8D3D4
FCEDEE

```html
<!DOCTYPE html>
<html lang="en">
<head>
<meta charset="utf-8">
<title>Gather Every Thread — Book Cover</title>
<link rel="stylesheet" href="https://fonts.googleapis.com/css2?family=Raleway:wght@200&family=Lato:wght@300&family=Dancing+Script:wght@500&display=swap">
<style>
  :root {
    --page-bg: #e6e6e6;
    --cover-top: #c7c4bc;
    --cover-bottom: #ebe9e5;
    --title-red: #ec5436;
    --ink: #1c1c1c;
    --band: #535353;
    --band-text: #f4f4f4;
    --art-edge: #b3b0aa;
    --art-mid: #7d7b77;
    --art-deep: #5c5a57;
  }
  * { margin: 0; padding: 0; box-sizing: border-box; }
  html, body {
    width: 1200px;
    height: 800px;
    overflow: hidden;
    background: var(--page-bg);
  }
  .canvas {
    position: relative;
    width: 1200px;
    height: 800px;
  }
  .cover {
    position: absolute;
    left: 365px;
    top: 42px;
    width: 470px;
    height: 716px;
    background: linear-gradient(to bottom, var(--cover-top) 0%, var(--cover-bottom) 80%);
    border-radius: 3px;
    overflow: hidden;
  }
  .title {
    position: absolute;
    top: 46px;
    left: 0;
    width: 100%;
    text-align: center;
    color: var(--title-red);
    font-family: "Raleway", sans-serif;
    font-weight: 200;
    text-transform: uppercase;
    line-height: 1;
  }
  .title-lead {
    display: block;
    font-size: 46px;
    letter-spacing: 0.02em;
  }
  .title-main {
    display: block;
    margin-top: 4px;
    font-size: 104px;
    letter-spacing: 0.01em;
  }
  .subtitle {
    position: absolute;
    top: 218px;
    left: 32px;
    width: 406px;
    text-align: center;
    color: var(--ink);
    font-family: "Dancing Script", cursive;
    font-weight: 500;
    font-size: 22px;
    line-height: 30px;
  }
  .cover-art {
    position: absolute;
    top: 326px;
    left: 30px;
    width: 410px;
    height: 262px;
  }
  .bottom-band {
    position: absolute;
    left: 0;
    bottom: 0;
    width: 470px;
    height: 118px;
  }
  .author {
    position: absolute;
    left: 0;
    bottom: 26px;
    width: 100%;
    text-align: center;
    color: var(--band-text);
    font-family: "Lato", sans-serif;
    font-weight: 300;
    font-size: 24px;
    letter-spacing: 0.32em;
    text-transform: uppercase;
  }
</style>
</head>
<body>
<main class="canvas">
  <section class="cover">
    <h1 class="title">
      <span class="title-lead">Gather Every</span>
      <span class="title-main">Thread</span>
    </h1>
    <p class="subtitle">Getting Ready Before Hard Times Strike (Including Final Goodbyes) for Every Household</p>

    <svg class="cover-art" role="img" aria-label="Illustration: two swirling flocks of small dark birds forming reaching shapes around a small red sun" viewBox="0 0 410 262">
      <defs>
        <linearGradient id="flockTone" x1="0" y1="0" x2="1" y2="1">
          <stop offset="0%" stop-color="var(--art-edge)"/>
          <stop offset="55%" stop-color="var(--art-mid)"/>
          <stop offset="100%" stop-color="var(--art-deep)"/>
        </linearGradient>
      </defs>
      <rect width="410" height="262" rx="10" fill="url(#flockTone)" opacity="0.8"/>
    </svg>

    <svg class="bottom-band" viewBox="0 0 470 118" preserveAspectRatio="none" aria-hidden="true">
      <path fill="var(--band)" d="M0 6 C40 2 70 8 110 14 C150 20 160 2 190 4 C220 6 235 16 265 14 C290 12 300 -2 330 2 C355 6 370 14 395 10 C420 6 440 8 470 12 L470 118 L0 118 Z"/>
    </svg>
    <p class="author">Marisa Holloway</p>
  </section>
</main>
</body>
</html>
```